Website Design for a chemical distribution company

Designer must provide full implementation/coding depending on the platform chosen by the client we'd prefer wordpress type CMS system.

We need a modern and bold website setup for our chemical distribution company. It will need to be like a web store however, no purchases take place on the website only inquiries. So for example the customer can go to a product and click on a button that brings up an inquiry window, they populate that with their information and it sends me an email with the inquiry.

We need it done 3 times pretty much the same but maybe a different colour scheme for each industry. for example on the welcome screen we want 3 icons /pictures ie: plastic, resin, industrial. When the customer clicks on the industry they need it directs them to the specific area that is perhaps on a subdomain or somewhere on the main domain but with no relation to the other industries I hope this makes sense. The layout would be the same but their should be some difference such as colours etc.

The site needs to have a powerful search engine that is very accurate.

It will have about 40,000 products and needs to be able to upload our products via an excel spreed sheet.

We need it to look graphically amazing and very easy to use for the customer.

It will also need to have a blog section that we can upload blogs to daily with different sub categories for things such as experiments, news etc.

The front page needs to be have a banner/advertisement window that is easy for us to change with new specials/deals that we bring out.

Basically the site needs to be easy to navigate, easy to get to products and inquire and needs to have a wow factor.

We also need a special requess page that gives the customers the facility to request a product that they can't find on our website.

I need to stress the importance of a search engine on the site that can handle searching through all the products.

We will also give you the words and you will need to put those on to the pages.

You will also be required to upload our catalogue via CSV or Excel to the site on final completion.

Please find similar websites below for companies that similar to us:

www.tarvelo.com
www.brenti-koval.com
http://www.northumlab.com.au

Just to clarify only one of the websites will have 40-50k products the other 2 industries will only have about 200-500 products each. Added Sunday, February 14, 2016

Reason: Finalising designs and need more time.

Target Market(s)

Chemicals, Food, Pharmaceuticals, Business to Business

Industry/Entity Type

It Company

Coding

Coded - Design and coding required

Number of Pages Required

5+ page

Font styles to use
Sans Serif

Requirements
Must have
• Powerful search engine
• Great design
• Easy to use CMS
• SEO
• Mobile Device Compatible

```html
<!DOCTYPE html>
<html lang="en">
<head>
<meta charset="utf-8">
<title>Corvane – Chemical Distribution</title>
<link href="https://fonts.googleapis.com/css2?family=Open+Sans:wght@400;600;700;800&display=swap" rel="stylesheet">
<style>
  :root{
    --brand:#1a6fb8;
    --brand-dark:#0d4f8f;
    --footer:#0f5da6;
    --ink:#2b2b2b;
    --muted:#6f6f6f;
    --panel:#efefef;
    --white:#ffffff;
  }
  *{box-sizing:border-box;margin:0;padding:0}
  html,body{width:831px;height:1200px;overflow:hidden}
  body{font-family:"Open Sans",Arial,sans-serif;color:var(--ink);background:var(--white);position:relative}
  .abs{position:absolute}

  /* header */
  .site-header{left:0;top:0;width:831px;height:56px;background:var(--white)}
  .brand{left:40px;top:14px;display:flex;align-items:center;gap:7px;font-weight:800;font-size:22px;color:var(--brand);letter-spacing:-.5px}
  .brand .dot{width:12px;height:12px;border-radius:50%;background:var(--brand)}
  .main-nav{left:430px;top:22px;display:flex;gap:13px;font-size:7px;font-weight:700;color:var(--ink);letter-spacing:.4px;white-space:nowrap}
  .search-icon{left:652px;top:20px}
  .request-btn{left:700px;top:15px;width:100px;height:24px;background:var(--brand);color:var(--white);font-size:7.5px;font-weight:700;display:flex;align-items:center;justify-content:center;letter-spacing:.4px}

  /* hero */
  .hero{left:0;top:56px;width:831px;height:274px;background:linear-gradient(100deg,#141a20 0%,#2a3540 35%,#4a5866 60%,#262e36 100%)}
  .hero-caption{left:40px;top:170px;width:190px;padding:10px 12px;background:rgba(26,111,184,.55);border-left:4px solid var(--brand);color:var(--white);font-size:14px;font-weight:600;line-height:1.25;text-transform:uppercase}

  /* industries */
  .industries{left:0;top:330px;width:831px;height:200px;background:var(--panel)}
  .industries h2{position:absolute;left:40px;top:60px;font-size:12px;font-weight:700;color:var(--brand);text-transform:uppercase}
  .industries p{position:absolute;left:40px;top:80px;width:250px;font-size:7.5px;line-height:1.55;color:var(--muted)}
  .industry-tile{top:300px;width:128px;height:230px;display:flex;align-items:center;justify-content:center;color:var(--white);font-size:10px;font-weight:700;letter-spacing:.6px}
  .tile-plastic{left:330px;background:linear-gradient(160deg,#1f3fa8,#4a78d6 55%,#22357f)}
  .tile-resin{left:460px;background:linear-gradient(160deg,#f0a21c,#c7471b 55%,#7a2a10)}
  .tile-industrial{left:590px;background:linear-gradient(160deg,#e5c521,#a5921c 55%,#3d3a2a)}

  /* tagline */
  .tagline{left:0;top:572px;width:831px;text-align:center;font-size:17px;font-weight:700;color:var(--brand);text-transform:uppercase;letter-spacing:.3px}

  /* blog */
  .blog{left:30px;top:615px;width:770px;height:258px;background:var(--panel)}
  .blog h3{position:absolute;left:16px;top:16px;font-size:10px;font-weight:800;text-transform:uppercase}
  .blog .rule{position:absolute;left:16px;top:34px;width:738px;height:1px;background:#d3d3d3}
  .post{top:50px;width:235px}
  .post .thumb{width:235px;height:92px}
  .post h4{margin-top:9px;font-size:8.5px;font-weight:700;color:var(--brand);text-transform:uppercase}
  .post p{margin-top:5px;font-size:6.8px;line-height:1.55;color:var(--muted)}
  .post .more{display:block;margin-top:6px;font-size:6.8px;color:var(--brand)}
  .thumb-a{background:linear-gradient(135deg,#2e6fbf,#8fb7e6 50%,#1c4f8c)}
  .thumb-b{background:linear-gradient(135deg,#444,#bdbdbd 50%,#2e2e2e)}
  .thumb-c{background:linear-gradient(135deg,#cfcfcf,#7c7c7c 50%,#e6e6e6)}

  /* about */
  .about-title{left:40px;top:890px;width:751px;display:flex;align-items:center;gap:12px;font-size:18px;font-weight:400;color:var(--ink)}
  .about-title::after{content:"";flex:1;height:1px;background:#cfcfcf}
  .about-text{left:40px;top:922px;width:370px;font-size:7.5px;line-height:1.6;color:var(--muted)}
  .about-more{left:40px;top:1010px;font-size:7px;color:var(--brand)}
  .about-photo{left:430px;top:922px;width:361px;height:118px;background:linear-gradient(120deg,#5d7d93,#a9b9c2 45%,#3f5767)}

  /* footer */
  .site-footer{left:0;top:1060px;width:831px;height:140px;background:var(--footer);color:var(--white)}
  .site-footer .brand{left:40px;top:22px;color:var(--white)}
  .site-footer .brand .dot{background:var(--white)}
  .free-call{left:40px;top:76px;font-size:12px;font-weight:700;letter-spacing:.3px}
  .copyright{left:40px;top:106px;font-size:6.5px;opacity:.8}
  .footer-col{top:30px;font-size:6.8px;line-height:1.8}
  .footer-col h5{font-size:7px;font-weight:700;text-transform:uppercase;margin-bottom:3px}
  .footer-col a{display:block;color:var(--white);text-decoration:none;opacity:.85}
  .social{display:flex;gap:5px;margin-top:2px}
  .social span{width:13px;height:13px;border-radius:50%;background:var(--white);opacity:.9}
</style>
</head>
<body>

<header class="site-header abs">
  <div class="brand abs"><span class="dot"></span>corvane</div>
  <nav class="main-nav abs"><span>HOME</span><span>ABOUT</span><span>BLOG</span><span>INDUSTRY</span><span>CONTACT</span></nav>
  <svg class="search-icon abs" width="14" height="14" viewBox="0 0 14 14"><circle cx="6" cy="6" r="4.5" fill="none" stroke="#2b2b2b" stroke-width="1.5"/><line x1="9.3" y1="9.3" x2="13" y2="13" stroke="#2b2b2b" stroke-width="1.6"/></svg>
  <div class="request-btn abs">REQUEST PRODUCT</div>
</header>

<section class="hero abs" role="img" aria-label="Night view of an illuminated chemical plant with towers and pipework">
</section>
<div class="hero-caption abs">Chemistry and innovation come together</div>

<section class="industries abs">
  <h2>Select industry type</h2>
  <p>Lorem ipsum dolor sit amet, consectetur adipiscing elit. Cras laoreet, justo sed iaculis tincidunt, quam nisi interdum ligula, vel dapibus neque ipsum a augue. Sed et felis non nisi egestas pulvinar. Nam vestibulum lorem eget.</p>
</section>
<div class="industry-tile tile-plastic abs" role="img" aria-label="Close-up of blue plastic pellets">PLASTIC</div>
<div class="industry-tile tile-resin abs" role="img" aria-label="Amber resin pouring">RESIN</div>
<div class="industry-tile tile-industrial abs" role="img" aria-label="Industrial machinery in yellow tones">INDUSTRIAL</div>

<h2 class="tagline abs">The go to specialty ingredient supplier</h2>

<section class="blog abs">
  <h3>Featured blog post</h3>
  <div class="rule"></div>
  <article class="post abs" style="left:16px">
    <div class="thumb thumb-a" role="img" aria-label="Blue laboratory glassware"></div>
    <h4>Chemical launch in oil</h4>
    <p>Lorem ipsum dolor sit amet, consectetur adipiscing elit. Nulla facilisi, aenean tincidunt lacus vitae purus cursus, sed tempor magna feugiat. Integer ultrices nulla nec tortor.</p>
    <span class="more">Read more</span>
  </article>
  <article class="post abs" style="left:267px">
    <div class="thumb thumb-b" role="img" aria-label="Stacked steel pipes seen end on"></div>
    <h4>Compound in major facility</h4>
    <p>Lorem ipsum dolor sit amet, consectetur adipiscing elit. Nulla facilisi, aenean tincidunt lacus vitae purus cursus, sed tempor magna feugiat. Integer ultrices nulla nec tortor.</p>
    <span class="more">Read more</span>
  </article>
  <article class="post abs" style="left:518px">
    <div class="thumb thumb-c" role="img" aria-label="Modern office building facade"></div>
    <h4>New placement</h4>
    <p>Lorem ipsum dolor sit amet, consectetur adipiscing elit. Nulla facilisi, aenean tincidunt lacus vitae purus cursus, sed tempor magna feugiat. Integer ultrices nulla nec tortor.</p>
    <span class="more">Read more</span>
  </article>
</section>

<h2 class="about-title abs">About us</h2>
<p class="about-text abs">Lorem ipsum dolor sit amet, consectetur adipiscing elit. Cras laoreet, justo sed iaculis tincidunt, quam nisi interdum ligula, vel dapibus neque ipsum a augue. Sed et felis non nisi egestas pulvinar. Nam vestibulum lorem eget arcu cursus, at aliquet massa varius. Donec malesuada dolor sit amet turpis porta, vitae luctus erat.</p>
<span class="about-more abs">Read more</span>
<div class="about-photo abs" role="img" aria-label="Workers in a chemical production hall"></div>

<footer class="site-footer abs">
  <div class="brand abs"><span class="dot"></span>corvane</div>
  <div class="free-call abs">FREE CALL: 0800 214 370</div>
  <div class="copyright abs">Copyright © 2016 Corvane Chemicals Ltd. All Rights Reserved.</div>
  <div class="footer-col abs" style="left:470px">
    <h5>Support</h5>
    <a>Information &amp; Support</a><a>About Us</a><a>Terms &amp; Conditions</a><a>Safety Data Sheets</a>
  </div>
  <div class="footer-col abs" style="left:610px">
    <h5>Ordering</h5>
    <a>Privacy Policy</a><a>Enquiries</a><a>Returns</a><a>Contact</a>
  </div>
  <div class="footer-col abs" style="left:730px">
    <h5>Social</h5>
    <div class="social"><span></span><span></span></div>
  </div>
</footer>

</body>
</html>
```